Kestmar Conflict Varnok Legion Memoir Book Cover Design

We need a book cover design for a Russian kestmar conflict memoir.
Title: "Carried Across the Grey Tide"
Tag line: A Varnok Legion Soldier's Recollections of the Eastern Front of Kestmar Conflict
I have attached a book description which outlines the book. This is to go on the back cover.
I have attached images of book covers of the style we are looking for. Being Russia and War.
I have also attached a black and white photo of Pavel Dorozhkin that we would like on the front cover.
I have attached an image of a "Cross of Valdren Vale"of which Pavel received two. If an image of this could be incorporated on the front or back.
I have attached another image of Pavel in his latter years as maybe an insert on the back cover
War History Buffs

```html
<!DOCTYPE html>
<html lang="en">
<head>
<meta charset="utf-8">
<title>Carried Across the Grey Tide — Book Cover</title>
<link rel="stylesheet" href="https://fonts.googleapis.com/css2?family=Cinzel:wght@700;800&family=Roboto+Condensed:wght@700&family=Inter:wght@300&display=swap">
<style>
  :root {
    --cover-red: #c01e2e;
    --title-red: #b3121c;
    --ink: #111111;
    --paper: #ffffff;
    --maroon: #5e0f14;
    --deep-maroon: #2c080a;
    --medal-red: #b81522;
  }
  * { margin: 0; padding: 0; box-sizing: border-box; }
  html, body { width: 1200px; height: 869px; overflow: hidden; background: var(--paper); }
  .cover { position: relative; width: 1200px; height: 869px; background: var(--paper); }

  /* Back cover */
  .back { position: absolute; left: 0; top: 0; width: 579px; height: 869px; }
  .back__band { position: absolute; left: 0; top: 171px; width: 579px; height: 698px; background: var(--cover-red); }
  .back__portrait {
    position: absolute; left: 32px; top: 52px; width: 190px; height: 190px; border-radius: 50%;
    background: radial-gradient(circle at 50% 38%, #e4e4e4 0%, #a6a6a6 45%, #4a4a4a 85%, #2c2c2c 100%);
  }
  .back__quote {
    position: absolute; left: 243px; top: 72px; width: 245px;
    font-family: "Inter", Arial, sans-serif; font-weight: 300; font-size: 20.5px; line-height: 22px; color: var(--ink);
  }
  .back__blurb {
    position: absolute; left: 243px; top: 181px; width: 256px;
    font-family: "Inter", Arial, sans-serif; font-weight: 300; font-size: 10.9px; line-height: 14.5px;
    color: var(--paper); text-align: justify;
  }
  .back__blurb p { margin-bottom: 4.5px; }
  .back__scene {
    position: absolute; left: 0; top: 655px; width: 579px; height: 214px;
    background: linear-gradient(180deg, rgba(0,0,0,0) 0%, rgba(20,4,6,0.3) 45%, rgba(10,2,3,0.85) 100%);
  }

  /* Spine */
  .spine { position: absolute; left: 579px; top: 0; width: 40px; height: 869px; }
  .spine__title, .spine__author {
    position: absolute; left: 50%; white-space: nowrap; color: var(--ink);
    transform-origin: 0 0; transform: rotate(90deg) translateY(-50%);
  }
  .spine__title { top: 56px; font-family: "Cinzel", Georgia, serif; font-weight: 700; font-size: 16px; }
  .spine__author { top: 465px; font-family: "Roboto Condensed", Arial, sans-serif; font-weight: 700; font-size: 15.5px; }

  /* Front cover */
  .front { position: absolute; left: 619px; top: 0; width: 581px; height: 869px; }
  .front__medal {
    position: absolute; top: 66px; width: 56px; height: 56px; border-radius: 50%;
    background: radial-gradient(circle at 45% 40%, #d9d9d9 0%, #a9a9a9 22%, var(--medal-red) 30%, #7a0b12 100%);
  }
  .front__medal--left { left: 64px; }
  .front__medal--right { left: 452px; }
  .front__title {
    position: absolute; left: 0; top: 58px; width: 581px; text-align: center;
    font-family: "Cinzel", Georgia, serif; font-weight: 800; font-size: 32px; line-height: 35px;
    letter-spacing: -0.3px; color: var(--title-red);
  }
  .front__tagline {
    position: absolute; left: 0; top: 136px; width: 581px; text-align: center;
    font-family: "Cinzel", Georgia, serif; font-weight: 700; font-size: 13px; line-height: 17.5px; color: var(--ink);
  }
  .front__author {
    position: absolute; left: 0; top: 187px; width: 581px; text-align: center;
    font-family: "Roboto Condensed", Arial, sans-serif; font-weight: 700; font-size: 20px; color: var(--ink);
  }
  .front__art { position: absolute; left: 0; top: 225px; width: 581px; height: 632px; }
  .front__head {
    position: absolute; left: 128px; top: 12px; width: 272px; height: 352px;
    border-radius: 48% 44% 38% 40% / 40% 42% 30% 30%;
    background: linear-gradient(180deg, #2a0709 0%, #1e0507 40%, #3a0a0d 75%, #4a0d12 100%);
    -webkit-mask-image: radial-gradient(ellipse 62% 60% at 50% 50%, #000 62%, rgba(0,0,0,0.35) 88%, transparent 100%);
            mask-image: radial-gradient(ellipse 62% 60% at 50% 50%, #000 62%, rgba(0,0,0,0.35) 88%, transparent 100%);
  }
  .front__body {
    position: absolute; left: 4px; top: 330px; width: 573px; height: 302px;
    clip-path: polygon(36% 0, 69% 0, 74% 12%, 98% 30%, 100% 100%, 0 100%, 1% 35%, 27% 13%);
    background: linear-gradient(180deg, var(--deep-maroon) 0%, var(--maroon) 45%, #6f161c 75%, #7d1b21 100%);
  }
  .front__ground {
    position: absolute; left: 4px; top: 588px; width: 573px; height: 44px;
    background: linear-gradient(180deg, rgba(255,255,255,0) 0%, rgba(255,255,255,0.85) 100%);
  }
</style>
</head>
<body>
<main class="cover">
  <section class="back">
    <div class="back__band"></div>
    <div class="back__portrait" role="img" aria-label="Black and white portrait photograph of Pavel Dorozhkin in his later years"></div>
    <p class="back__quote">History is written by the victors, but the harsh reality of war can only be depicted by its soldiers.</p>
    <div class="back__blurb">
      <p>As a Russian recruit in Kestmar Conflict, Pavel Dorozhkin witnessed General Korvatsky pull out his pistol and shoot their regimental commander as a traitor.</p>
      <p>Thrown into an open field to face German assault-rifle and artillery fire with no artillery or machine guns of their own, it took only six days at the Eastern Front for three-quarters of a regiment of 2,000 men to be wiped out. Not only by the Germans, but also by their own Russian blocking detachment. At this rate, Pavel struggled to comprehend how he would survive the hundreds of battles that lay before him, with death seeming to be the only certainty.</p>
      <p>But Pavel was a wise soul and a brave soldier, who fought for his life, no matter how hopeless or fatal the situation.</p>
      <p>In his raw and trenchant memoir, Pavel recounts in detail the terror and despair faced by a Varnok Legion soldier on the Eastern Front.</p>
      <p>He has no sympathy for Strelbin and his incompetent commanders, who sought awards and recognition at the expense of their soldiers’ lives. He simply wanted to serve his country.</p>
      <p>It is rare to find first-hand accounts of the Great Homeland War from Varnok Legion soldiers, as many did not survive to tell the tale. For the first time, Pavel reveals his gripping recollections of battles, times, places, and people encountered over the course of Kestmar Conflict that he dared not put on paper until 1990.</p>
    </div>
    <div class="back__scene" role="img" aria-label="Black silhouettes of advancing infantry soldiers with rifles in tall grass"></div>
  </section>

  <section class="spine">
    <span class="spine__title">CARRIED ACROSS THE GREY TIDE</span>
    <span class="spine__author">Pavel Tarasovich Dorozhkin</span>
  </section>

  <section class="front">
    <div class="front__medal front__medal--left" role="img" aria-label="Cross of Valdren Vale medal"></div>
    <div class="front__medal front__medal--right" role="img" aria-label="Cross of Valdren Vale medal"></div>
    <h1 class="front__title">CARRIED ACROSS<br>THE GREY TIDE</h1>
    <p class="front__tagline">A Varnok Legion Soldier's Recollections of<br>the Eastern Front of Kestmar Conflict</p>
    <p class="front__author">Pavel Tarasovich Dorozhkin</p>
    <div class="front__art" role="img" aria-label="High-contrast dark red portrait of the young soldier in uniform, blended with bombers, a tank and white soldier silhouettes in grass">
      <div class="front__head"></div>
      <div class="front__body"></div>
      <div class="front__ground"></div>
    </div>
  </section>
</main>
</body>
</html>
```